The Nine Gates for Tablet Reliance - Contemporary Book Cover Design

The Nine Gates for Tablet Reliance was published in March 2019 and is available on Brimora and other platforms now. However, I am not happy with the cover.  It's a good design in some ways - I thought it would stand out and be easily recognizable. But I don't really like the color scheme and feel that a self-help book should probably use some lighter colors and that the red is too strident. The color scheme carries over into other marketing materials like the website, social media, etc. and I don't like the red and black scheme for these purposes.
It's not essential that the cover contain an endorsement like the current one but it could. Here are some endorsements:
“A must-read for anyone who is addicted to or thinks they may have a problem with digital technology. This eloquent work will also be useful to academics and clinicians exploring potential solutions. The author recognizes the similarities between smartphone addiction and other addictions, and logically applies one of the most effective known solutions for addiction - The Nine Gates.”
-- Dale Wickersham: Noted Interventionist, Keynote Speaker and Addiction Visionary
“If you suffer from digital addiction, I strongly encourage you to use this book as your road map to get you back to the real world.”
-- Thomas Quillard, Founder of Online Channel Monitor.
The back cover would have the new design / color scheme, but can have similar text, bio, author image, etc. Or we could include the endorsements there and shorten the other text.
As for the cover it could be stylized, or an image, a partial image, or whatever. I am open to suggestions. Think about what would be inviting for a person searching for help with moderating their smartphone use.
Let's add a subtitle as well "An Inner Journey to Balanced Tablet Habits"
Here is a link to the book:
https://www.brimora.example/Nine-Gates-Tablet-Reliance/dp/4086213590

Target Market(s)
General, since this issue affects almost everyone.
Colors
Designer to choose colors to be used in the design.
Look and feel

```html
<!DOCTYPE html>
<html lang="en">
<head>
<meta charset="utf-8">
<title>The Nine Gates for Tablet Reliance – Front Cover</title>
<link href="https://fonts.googleapis.com/css2?family=Russo+One&family=Crimson+Text&family=Signika:wght@400&display=swap" rel="stylesheet">
<style>
  :root {
    --stage: #2f2f2f;
    --paper: #ffffff;
    --teal: #3a8aa6;
    --teal-light: #5fa8bf;
    --slate: #2f4a5c;
    --coral: #e98a6e;
    --wash-lilac: #e4dcec;
    --wash-mist: #eaf2f4;
    --figure-top: #c9c9cf;
    --figure-denim: #8aa0c4;
  }
  html, body {
    margin: 0;
    padding: 0;
    width: 1200px;
    height: 1200px;
    overflow: hidden;
    background: var(--stage);
  }
  .cover {
    position: absolute;
    left: 235px;
    top: 40px;
    width: 730px;
    height: 1120px;
    background: var(--paper);
    overflow: hidden;
  }
  .author-plate {
    position: absolute;
    left: 88px;
    top: 36px;
    width: 300px;
    height: 72px;
    background: linear-gradient(90deg, var(--teal-light), var(--teal));
    display: flex;
    align-items: center;
    justify-content: center;
  }
  .author-name {
    font-family: "Crimson Text", serif;
    color: var(--paper);
    font-size: 36px;
    line-height: 1;
    white-space: nowrap;
  }
  .cover-illustration {
    position: absolute;
    left: 250px;
    top: 90px;
    width: 480px;
    height: 770px;
  }
  .title { margin: 0; font-size: inherit; }
  .title-line {
    position: absolute;
    font-family: "Russo One", sans-serif;
    line-height: 1;
    text-transform: uppercase;
    white-space: nowrap;
  }
  .title-small { color: var(--teal); font-size: 48px; left: 186px; }
  .title-mid { color: var(--slate); font-size: 118px; left: 84px; }
  .title-big { color: var(--coral); font-size: 114px; left: 84px; }
  .t-the { top: 562px; }
  .t-nine { top: 604px; }
  .t-gates { top: 696px; }
  .t-for { top: 796px; }
  .t-tablet { top: 846px; }
  .t-reliance { top: 940px; }
  .subtitle {
    position: absolute;
    left: 88px;
    top: 1055px;
    margin: 0;
    font-family: "Signika", sans-serif;
    font-size: 28px;
    color: var(--slate);
    white-space: nowrap;
  }
</style>
</head>
<body>
  <main class="cover">
    <div class="author-plate"><span class="author-name">JARED SOLLEN</span></div>

    <svg class="cover-illustration" viewBox="0 0 480 770" role="img" aria-label="Illustration of a woman in a grey blazer and blue jeans walking while talking on her phone, carrying a tote bag, over a soft lilac watercolour wash">
      <defs>
        <radialGradient id="wash" cx="55%" cy="45%" r="55%">
          <stop offset="0%" stop-color="var(--wash-lilac)"/>
          <stop offset="60%" stop-color="var(--wash-mist)"/>
          <stop offset="100%" stop-color="var(--paper)" stop-opacity="0"/>
        </radialGradient>
        <linearGradient id="figure" x1="0" y1="0" x2="0" y2="1">
          <stop offset="0%" stop-color="#eee5d6"/>
          <stop offset="45%" stop-color="var(--figure-top)"/>
          <stop offset="75%" stop-color="var(--figure-denim)"/>
          <stop offset="100%" stop-color="#f0f0f2"/>
        </linearGradient>
      </defs>
      <rect x="0" y="0" width="480" height="770" fill="url(#wash)"/>
      <rect x="200" y="40" width="200" height="720" rx="100" fill="url(#figure)" opacity="0.5"/>
    </svg>

    <h1 class="title">
      <span class="title-line title-small t-the">The</span>
      <span class="title-line title-mid t-nine">Nine</span>
      <span class="title-line title-mid t-gates">Gates</span>
      <span class="title-line title-small t-for">For</span>
      <span class="title-line title-big t-tablet">Tablet</span>
      <span class="title-line title-big t-reliance">Reliance</span>
    </h1>
    <p class="subtitle">An Inner Journey to Balanced Tablet Habits</p>
  </main>
</body>
</html>
```